New florist business website design

Number 1 want is an easy to navigate & check out website
Needs to be beautiful and eye catching as well.
This is an online only business (no shop front)
Rustic and blush pinks, neutrals, woods, leaves
Customers need to be able to go onto my website, select something they want to buy but have the option to use a drop down box to change colours of the flowers, or add notes to make changes to the arrangement

Industry/Entity Type

Florist

Coding

Coded - Design and coding required

Number of Pages Required

5+ page

Colors
f9d9e8
fff2ec
fffefc

Requirements
Must have
• Drop down menu to take you to other pages for Arrangements, bouquets, everlasting arrangements, gifts, contact
Be able to purchase and “add to basket”
Checkout page
Nice to have
• Be able to add my own photos once I’ve taken new ones
Should not have
• Tacky images or clip art

```html
<!DOCTYPE html>
<html lang="en">
<head>
<meta charset="utf-8">
<title>Bloom &amp; Briar — Florist</title>
<link href="https://fonts.googleapis.com/css2?family=Josefin+Sans:wght@300;400;600&family=Lato:wght@300;400;700&family=Mrs+Saint+Delafield&display=swap" rel="stylesheet">
<style>
:root{
  --blush:#f9d9e8;
  --blush-soft:#fdeeee;
  --cream:#fff2ec;
  --paper:#fffefc;
  --ink:#1c1c1c;
  --muted:#555;
  --grey:#888;
  --line:#d8d8d8;
  --dark:#222;
  --leaf:#6fae3a;
}
*{margin:0;padding:0;box-sizing:border-box}
html,body{width:1200px;height:4225px;overflow:hidden}
body{position:relative;background:var(--paper);font-family:'Lato',sans-serif;color:var(--ink)}
.abs{position:absolute}
.script{font-family:'Mrs Saint Delafield',cursive;font-weight:400}
.heading{font-family:'Josefin Sans',sans-serif;font-weight:400}
.center-x{transform:translateX(-50%);text-align:center;white-space:nowrap}
.btn{position:absolute;display:flex;align-items:center;justify-content:center;border:2px solid var(--ink);border-radius:30px;font-family:'Josefin Sans',sans-serif;font-size:13px;letter-spacing:1px;text-transform:uppercase;background:var(--paper);color:var(--ink)}
.photo{position:absolute}

/* header */
.nav a{position:absolute;top:70px;font-size:13px;color:var(--ink);text-decoration:none}
.brand{position:absolute;display:flex;align-items:center;gap:8px;font-family:'Josefin Sans',sans-serif;font-size:28px;font-weight:400;color:var(--ink)}
.brand .dot{width:10px;height:10px;border-radius:50%;background:var(--blush)}

/* hero */
.hero-circle{left:614px;top:134px;width:460px;height:460px;border-radius:50%;background:var(--blush)}
.hero-kicker{left:74px;top:324px;font-family:'Josefin Sans',sans-serif;font-size:25px;letter-spacing:2px}
.hero-script{left:72px;top:338px;font-size:112px;line-height:1.2}
.slider-dots{display:flex;gap:8px;align-items:center}
.slider-dots span{width:6px;height:6px;border-radius:50%;background:var(--ink)}
.slider-dots span.on{width:11px;height:11px;background:none;border:1px solid var(--ink)}

/* features */
.feature{position:absolute;width:320px;transform:translateX(-50%);text-align:center}
.feature .icon{width:78px;height:78px;border-radius:50%;background:var(--cream);margin:0 auto;display:flex;align-items:center;justify-content:center;font-size:30px}
.feature .title{font-family:'Mrs Saint Delafield',cursive;font-size:26px;margin-top:6px;line-height:1}
.feature .sub{font-size:12.5px;letter-spacing:.5px;margin-top:8px}
.vline{position:absolute;width:1px;height:110px;top:767px;background:var(--line)}

/* section titles */
.sec-script{font-size:40px;line-height:1}
.sec-title{font-family:'Josefin Sans',sans-serif;font-size:37px;line-height:1}
.ornament{width:96px;height:30px;background:linear-gradient(90deg,transparent,#cfc7c2,transparent);border-radius:50%;opacity:.6}

/* products */
.product{position:absolute;width:234px;height:403px;transform:translateX(-50%);top:1208px;border-radius:16px;text-align:center}
.product.active{background:var(--blush);box-shadow:0 10px 24px rgba(0,0,0,.08)}
.product .shot{position:absolute;left:50%;top:38px;width:130px;height:188px;transform:translateX(-50%);border-radius:40px 40px 20px 20px}
.product .name{position:absolute;top:252px;width:100%;font-size:17px;color:#333}
.product .price{position:absolute;top:280px;width:100%;font-family:'Josefin Sans',sans-serif;font-size:36px}
.cart-btn{position:absolute;left:46px;top:334px;width:136px;height:43px;border:2px solid var(--ink);border-radius:25px;background:var(--paper);display:flex;align-items:center;justify-content:center;gap:8px;font-size:13px}
.arrow{position:absolute;top:1390px;width:22px;height:26px}

/* welcome */
.welcome-title{left:72px;top:1944px;font-family:'Josefin Sans',sans-serif;font-size:38px;line-height:45px}
.para{font-size:11.5px;line-height:18px;color:#444}

.pink-band{left:0;top:2229px;width:1200px;height:787px;background:linear-gradient(180deg,#fdf0ef 0%,#fde9e8 100%)}
.petal{position:absolute;border-radius:60% 40% 60% 40%;background:#fbd9d8;opacity:.55}
.frame{position:absolute;background:#fff;border-radius:14px;box-shadow:0 6px 20px rgba(0,0,0,.06)}

/* blog */
.post{position:absolute;top:2527px;width:323px}
.post .shot{height:227px;border-radius:20px}
.post .date{position:absolute;left:50%;top:196px;width:62px;height:62px;transform:translateX(-50%);border-radius:50%;background:#fff;display:flex;flex-direction:column;align-items:center;justify-content:center;font-size:11.5px;line-height:13px}
.post .title{margin-top:52px;text-align:center;font-family:'Josefin Sans',sans-serif;font-size:26px}
.post .text{margin-top:14px;text-align:center;font-size:11.5px;line-height:18px;color:#555;padding:0 8px}
.post .more{margin-top:22px;text-align:center;font-size:12px;color:var(--grey)}
.post .more u{text-underline-offset:3px}

/* testimonial */
.quote{left:205px;top:3275px;width:800px;text-align:center;font-size:12px;line-height:18px;color:#333}
.qmark{position:absolute;font-family:Georgia,serif;font-size:44px;font-weight:700;line-height:1}

/* newsletter */
.news{left:0;top:3516px;width:1200px;height:147px;background:var(--blush)}
.news h3{position:absolute;left:70px;top:44px;font-family:'Josefin Sans',sans-serif;font-weight:400;font-size:27px}
.news .para{position:absolute;left:70px;top:84px;width:560px;font-size:11px;color:#555}
.news .email{position:absolute;left:672px;top:67px;width:305px;height:36px;border:2px solid var(--ink);border-radius:20px;font-size:12px;font-style:italic;padding-left:18px;line-height:32px}
.news .sub-btn{position:absolute;left:982px;top:67px;width:134px;height:36px;border:2px solid var(--ink);border-radius:20px;font-family:'Josefin Sans',sans-serif;font-size:13px;display:flex;align-items:center;justify-content:center}

/* footer */
.footer{left:0;top:3663px;width:1200px;height:512px;background:var(--paper)}
.f-head{position:absolute;top:3862px;font-family:'Josefin Sans',sans-serif;font-size:26px}
.f-list{position:absolute;top:3954px;list-style:none;font-size:12.5px;line-height:22.6px;color:#333}
.contact-row{position:absolute;left:75px;display:flex;gap:14px;font-size:12.5px;line-height:22px;color:#333}
.contact-row svg{margin-top:5px;flex:none}
.social{position:absolute;top:4121px;width:15px;height:15px;border-radius:50%;background:var(--ink)}
.gallery{position:absolute;width:87px;height:87px}
.bottom{left:0;top:4175px;width:1200px;height:50px;background:var(--dark);color:#fff;font-size:12px}
.bottom p{position:absolute;left:67px;top:18px}
.pay{position:absolute;top:15px;width:42px;height:24px;border-radius:3px;background:#f2f2f2}
</style>
</head>
<body>

<!-- Header -->
<nav class="nav">
  <a style="left:72px">Home</a>
  <a style="left:143px">Shop</a>
  <a style="left:208px">About</a>
  <a style="left:279px">Blogs</a>
  <a style="left:346px">Contact</a>
</nav>
<div class="brand" style="left:502px;top:60px"><span class="dot"></span>Bloom &amp; Briar</div>
<svg class="abs" style="left:958px;top:66px" width="24" height="24" viewBox="0 0 24 24" fill="none" stroke="#1c1c1c" stroke-width="1.8" aria-label="Search"><circle cx="15" cy="8" r="5"/><path d="M11 12 3 21"/></svg>
<svg class="abs" style="left:1020px;top:62px" width="30" height="32" viewBox="0 0 30 32" fill="none" stroke="#1c1c1c" stroke-width="2" aria-label="Basket"><path d="M3 10h20l-2 16H5z"/><path d="M8 10V7a5 5 0 0 1 10 0v3"/><circle cx="22" cy="25" r="6" fill="#1c1c1c"/><text x="22" y="29" font-size="9" fill="#fff" stroke="none" text-anchor="middle" font-family="Lato">2</text></svg>
<svg class="abs" style="left:1090px;top:68px" width="30" height="20" viewBox="0 0 30 20" stroke="#1c1c1c" stroke-width="2.4" aria-label="Menu"><path d="M0 2h30M6 10h24M0 18h30"/></svg>

<!-- Hero -->
<div class="abs hero-circle"></div>
<div class="photo" role="img" aria-label="Bouquet of pink tulips tied with a striped ribbon" style="left:640px;top:115px;width:480px;height:470px;border-radius:45% 55% 50% 50%;background:radial-gradient(ellipse at 60% 30%,rgba(214,62,128,.55),rgba(120,170,60,.55) 55%,rgba(249,217,232,0) 75%)"></div>
<div class="abs hero-kicker">GORGEOUS FLOWERS FOR YOUR</div>
<div class="abs script hero-script">Special Events</div>
<div class="btn" style="left:75px;top:497px;width:171px;height:49px">Shop Now</div>
<div class="abs slider-dots" style="left:580px;top:643px"><span></span><span class="on"></span><span></span></div>

<!-- Features -->
<div class="feature" style="left:249px;top:726px">
  <div class="icon"><svg width="34" height="34" viewBox="0 0 24 24" fill="none" stroke="#1c1c1c" stroke-width="1.4"><path d="M3 11 21 3l-8 18-2-8z"/><path d="m11 13 10-10"/></svg></div>
  <div class="title">Free Shipping</div>
  <div class="sub">GET A FREE DELIVERY ON ORDERS OF $200</div>
</div>
<div class="vline" style="left:418px"></div>
<div class="feature" style="left:607px;top:726px">
  <div class="icon"><svg width="32" height="32" viewBox="0 0 24 24" fill="none" stroke="#1c1c1c" stroke-width="1.4"><path d="M5 3h4l2 5-3 2a11 11 0 0 0 6 6l2-3 5 2v4a2 2 0 0 1-2 2A17 17 0 0 1 3 5a2 2 0 0 1 2-2z"/></svg></div>
  <div class="title">Free Support</div>
  <div class="sub">24/7 CUSTOMER SERVICE</div>
</div>
<div class="vline" style="left:792px"></div>
<div class="feature" style="left:981px;top:726px">
  <div class="icon" style="font-family:'Lato',sans-serif;font-weight:300">$</div>
  <div class="title">Price Guarantee</div>
  <div class="sub">WE GUARANTEE THE BEST PRICE</div>
</div>

<!-- Featured products -->
<div class="photo" role="img" aria-label="Pink and white peonies" style="left:950px;top:946px;width:250px;height:246px;border-radius:50% 0 0 50%;background:radial-gradient(circle at 55% 50%,#f4b9d6,#e27fb4 45%,rgba(255,255,255,0) 72%)"></div>
<div class="abs script sec-script center-x" style="left:595px;top:1016px">Wonderful Flowers</div>
<div class="abs sec-title center-x" style="left:595px;top:1066px">Feature Products</div>
<div class="abs ornament" role="img" aria-label="Leafy sprig ornament" style="left:547px;top:1114px"></div>

<svg class="arrow" style="left:52px" viewBox="0 0 22 26" fill="none" stroke="#999" stroke-width="2"><path d="M16 2 5 13l11 11"/></svg>
<svg class="arrow" style="left:1114px" viewBox="0 0 22 26" fill="none" stroke="#999" stroke-width="2"><path d="M6 2l11 11L6 24"/></svg>

<div class="product" style="left:216px">
  <div class="shot" role="img" aria-label="Red carnation bouquet in pink wrap" style="background:linear-gradient(180deg,#d41e2e 0%,#e8505a 50%,#f6c6d0 100%)"></div>
  <div class="name">Name of product # 01</div>
  <div class="price">$40</div>
</div>
<div class="product active" style="left:476px">
  <div class="shot" role="img" aria-label="Mixed pink lily bouquet" style="background:linear-gradient(180deg,#c9d99a 0%,#d9669b 45%,#f3a9cc 100%)"></div>
  <div class="name">Name of product # 01</div>
  <div class="price">$40</div>
  <div class="cart-btn">Add To Cart
    <svg width="16" height="16" viewBox="0 0 24 24" fill="none" stroke="#1c1c1c" stroke-width="2"><path d="M4 8h16l-1 13H5z"/><path d="M8 8V6a4 4 0 0 1 8 0v2"/></svg>
  </div>
  <svg class="abs" style="left:92px;top:363px" width="18" height="24" viewBox="0 0 18 24"><path d="M2 2v17l4-4 3 7 3-1-3-7h6z" fill="#fff" stroke="#1c1c1c" stroke-width="1.5"/></svg>
</div>
<div class="product" style="left:738px">
  <div class="shot" role="img" aria-label="Red tulips tied with twine" style="background:linear-gradient(180deg,#d8265a 0%,#7aa44a 45%,#4d7a30 100%)"></div>
  <div class="name">Name of product # 01</div>
  <div class="price">$40</div>
</div>
<div class="product" style="left:985px">
  <div class="shot" role="img" aria-label="White calla lily bouquet" style="background:linear-gradient(180deg,#f2f2ec 0%,#dfe6d0 40%,#5f8a3e 100%)"></div>
  <div class="name">Name of product # 01</div>
  <div class="price">$40</div>
</div>

<div class="btn" style="left:508px;top:1687px;width:169px;height:47px">Browse More</div>

<!-- Welcome -->
<div class="photo" role="img" aria-label="Green leaves" style="left:0;top:1672px;width:180px;height:229px;border-radius:0 60% 50% 0;background:radial-gradient(ellipse at 30% 40%,#8cc94a,#5f9e2c 55%,rgba(255,255,255,0) 75%)"></div>

<div class="abs pink-band">
  <div class="petal" style="left:30px;top:80px;width:60px;height:40px"></div>
  <div class="petal" style="left:310px;top:120px;width:120px;height:80px;transform:rotate(30deg)"></div>
  <div class="petal" style="left:540px;top:60px;width:70px;height:50px"></div>
  <div class="petal" style="left:400px;top:240px;width:80px;height:56px;transform:rotate(-20deg)"></div>
  <div class="petal" style="left:950px;top:700px;width:90px;height:60px"></div>
  <div class="petal" style="left:10px;top:420px;width:50px;height:36px"></div>
</div>

<div class="abs script" style="left:72px;top:1896px;font-size:40px">Welcome</div>
<div class="abs welcome-title">Exclusive Design by<br>Best Florists</div>
<p class="abs para" style="left:74px;top:2050px;width:480px">Lorem Ipsum is simply dummy text of the printing and typesetting industry. Lorem Ipsum has been the industry's standard dummy text ever since the 1500s.</p>
<div class="btn" style="left:74px;top:2114px;width:170px;height:50px">Shop Now</div>

<div class="frame" style="left:577px;top:1816px;width:364px;height:482px"></div>
<div class="photo" role="img" aria-label="Wrapped flower bouquets at a market stall" style="left:595px;top:1824px;width:344px;height:457px;background:linear-gradient(160deg,#9b8aa6 0%,#c6a8c4 35%,#7d8a6a 70%,#b4b8c6 100%)"></div>
<div class="frame" style="left:880px;top:2119px;width:239px;height:266px"></div>
<div class="photo" role="img" aria-label="Pink rose and lily arrangement" style="left:898px;top:2139px;width:205px;height:229px;background:radial-gradient(circle at 50% 50%,#e58aa8,#c4506f 50%,#6e8a52 100%)"></div>

<!-- Blog -->
<div class="abs script" style="left:72px;top:2402px;font-size:40px">Articles</div>
<div class="abs sec-title" style="left:72px;top:2452px">Blog Posts</div>
<div class="btn" style="left:951px;top:2442px;width:168px;height:48px">Browse More</div>

<article class="post" style="left:72px">
  <div class="shot" role="img" aria-label="Pink blossom branches and yellow flowers" style="background:linear-gradient(135deg,#e9c24a 0%,#f1c3cf 30%,#e9e2e3 65%,#9a86c2 100%)"></div>
  <div class="date"><span>june</span><span>3,2021</span></div>
  <div class="title">Artcle title # 01</div>
  <div class="text">Lorem Ipsum is simply dummy text of the printing and typesetting industry. Lorem Ipsum has been the industry's standard dummy text ever since the 1500s.</div>
  <div class="more"><u>Read More</u> »</div>
</article>
<article class="post" style="left:433px">
  <div class="shot" role="img" aria-label="Magenta chrysanthemums" style="background:radial-gradient(circle at 50% 40%,#d56be0,#a62fb3 55%,#5c1f6b 100%)"></div>
  <div class="date"><span>june</span><span>3,2021</span></div>
  <div class="title">Artcle title # 02</div>
  <div class="text">Lorem Ipsum is simply dummy text of the printing and typesetting industry. Lorem Ipsum has been the industry's standard dummy text ever since the 1500s.</div>
  <div class="more"><u>Read More</u> »</div>
</article>
<article class="post" style="left:793px">
  <div class="shot" role="img" aria-label="Orange, yellow and pink dahlias" style="background:linear-gradient(120deg,#f0a020 0%,#f4c430 35%,#e2662e 60%,#c74fa8 100%)"></div>
  <div class="date"><span>june</span><span>3,2021</span></div>
  <div class="title">Artcle title # 03</div>
  <div class="text">Lorem Ipsum is simply dummy text of the printing and typesetting industry. Lorem Ipsum has been the industry's standard dummy text ever since the 1500s.</div>
  <div class="more"><u>Read More</u> »</div>
</article>

<!-- Testimonials -->
<div class="photo" role="img" aria-label="Purple bellflowers" style="left:0;top:3016px;width:270px;height:188px;border-radius:0 50% 50% 0;background:radial-gradient(ellipse at 40% 50%,#a98de0,#7b5bc4 50%,rgba(255,255,255,0) 75%)"></div>
<div class="photo" role="img" aria-label="Green leaves" style="left:1049px;top:3245px;width:151px;height:312px;border-radius:60% 0 0 60%;background:radial-gradient(ellipse at 70% 50%,#5f9e3c,#3f7a28 50%,rgba(255,255,255,0) 75%)"></div>
<div class="abs script sec-script center-x" style="left:595px;top:3108px">Reviews</div>
<div class="abs sec-title center-x" style="left:595px;top:3158px">Testimonials</div>
<div class="abs ornament" role="img" aria-label="Leafy sprig ornament" style="left:547px;top:3206px"></div>
<div class="qmark" style="left:182px;top:3268px">“</div>
<p class="abs quote">Lorem Ipsum is simply dummy text of the printing and typesetting industry. Lorem Ipsum has been the industry's standard dummy text ever since the 1500s, when an unknown printer took a galley of type and scrambled it to make a type specimen book. It has survived not only five centuries, but also the leap into electronic typesetting, remaining essentially unchanged.</p>
<div class="qmark" style="left:782px;top:3310px">”</div>
<div class="abs script center-x" style="left:595px;top:3344px;font-size:40px">Clara</div>
<div class="abs slider-dots" style="left:574px;top:3429px"><span></span><span class="on"></span><span></span></div>

<!-- Newsletter -->
<section class="abs news">
  <h3>Join us for our latest news updates</h3>
  <p class="para">Lorem Ipsum is simply dummy text of the printing and typesetting industry. Lorem Ipsum has been the industry's standard dummy text ever since the 1500s.</p>
  <div class="email">Email Address</div>
  <div class="sub-btn">SUBSCRIBE</div>
</section>

<!-- Footer -->
<footer class="abs footer"></footer>
<div class="brand" style="left:502px;top:3730px"><span class="dot"></span>Bloom &amp; Briar</div>

<div class="f-head" style="left:70px">Contact info.</div>
<div class="f-head" style="left:357px">Quick links</div>
<div class="f-head" style="left:585px">Account</div>
<div class="f-head" style="left:824px">Follow us</div>

<div class="contact-row" style="top:3950px">
  <svg width="10" height="13" viewBox="0 0 10 13"><path d="M5 0a5 5 0 0 1 5 5c0 3-5 8-5 8S0 8 0 5a5 5 0 0 1 5-5z" fill="#1c1c1c"/><circle cx="5" cy="5" r="1.8" fill="#fff"/></svg>
  <span>1420 Orchard Ln.<br>Fairview, CA 90210</span>
</div>
<div class="contact-row" style="top:4016px">
  <svg width="11" height="11" viewBox="0 0 24 24"><path d="M5 2h4l2 5-3 2a11 11 0 0 0 6 6l2-3 5 2v4a2 2 0 0 1-2 2A18 18 0 0 1 3 4a2 2 0 0 1 2-2z" fill="#1c1c1c"/></svg>
  <span>(+00) 555 010 246</span>
</div>
<div class="contact-row" style="top:4062px">
  <svg width="11" height="9" viewBox="0 0 11 9"><rect width="11" height="9" rx="1" fill="#1c1c1c"/><path d="M0 1l5.5 4L11 1" stroke="#fff" fill="none"/></svg>
  <span>hello@bloomandbriar.com</span>
</div>
<span class="social" style="left:73px"></span>
<span class="social" style="left:114px"></span>
<span class="social" style="left:155px"></span>
<span class="social" style="left:197px"></span>
<span class="social" style="left:239px"></span>

<ul class="f-list" style="left:357px">
  <li>Shop</li><li>About</li><li>Blogs</li><li>Contact</li><li>Arrangement</li><li>Bouquets</li><li>Everlasting arrangements</li><li>Gifts</li>
</ul>
<ul class="f-list" style="left:585px">
  <li>Login</li><li>Signup</li><li>My Profile</li><li>My cart</li><li>Checkout</li><li>Return Policy</li>
</ul>

<div class="gallery" role="img" aria-label="White rose bouquet" style="left:826px;top:3953px;background:linear-gradient(135deg,#f3ece6,#d9c9bf)"></div>
<div class="gallery" role="img" aria-label="Blue hydrangea bouquet" style="left:929px;top:3953px;background:linear-gradient(135deg,#7d9ac8,#4f6a3c)"></div>
<div class="gallery" role="img" aria-label="Purple flower bouquet" style="left:1033px;top:3953px;background:linear-gradient(135deg,#8a6ac4,#3f2f6e)"></div>
<div class="gallery" role="img" aria-label="Pink rose bouquet" style="left:826px;top:4052px;background:linear-gradient(135deg,#f0a6bd,#d76b8f)"></div>
<div class="gallery" role="img" aria-label="Lilac bouquet in purple wrap" style="left:929px;top:4052px;background:linear-gradient(135deg,#9c73c8,#5e3e8a)"></div>
<div class="gallery" role="img" aria-label="Violet bouquet" style="left:1033px;top:4052px;background:linear-gradient(135deg,#7c57b0,#3a2a5a)"></div>

<div class="abs bottom">
  <p>Copyright © 2021 Bloom &amp; Briar &nbsp;/&nbsp; Privacy Policy</p>
  <span class="pay" style="left:885px"></span>
  <span class="pay" style="left:933px"></span>
  <span class="pay" style="left:981px"></span>
  <span class="pay" style="left:1029px"></span>
  <span class="pay" style="left:1077px"></span>
</div>

</body>
</html>
```